Flyer Design Print Ad for Clothing Store

We are a modest women's clothing store. We are looking for a print ad 90*134 mm that is attention grabbing and can serve as a template for us going forward. We cannot use pictures of actual women. We need it to include our logo, store hours, physical address, website, phone number. We would use this template and change the call to action as necessary e. g. BOGO Sale, 30% off, flash sale, summer sale etc. Our colors are black and white and our fonts are Bodoni sans and Athens.

Target Market(s)

Women from teen to age 70

Industry/Entity Type

Women's clothing

Font styles to use
Other font styles liked:
• Athens, Bodoni Sans

Requirements
Must have
• Our, logo, phone number, website, address and store hours
Nice to have
• I'd like something that's not just our flat logo but something that will make someone pause to look
Should not have
• Pictures of women

```html
<!DOCTYPE html>
<html lang="en">
<head>
<meta charset="utf-8">
<title>Lumella Summer Sale Flyer</title>
<link rel="stylesheet" href="https://fonts.googleapis.com/css2?family=Marcellus&family=Varela+Round&display=swap">
<style>
  :root {
    --ink: #000000;
    --paper: #ffffff;
    --sale-red: #ec1c24;
    --bg-top: #000000;
    --bg-glow: #141414;
  }
  * { margin: 0; padding: 0; box-sizing: border-box; }
  html, body { width: 850px; height: 1200px; overflow: hidden; background: var(--ink); }
  .flyer {
    position: relative;
    width: 850px; height: 1200px;
    background: radial-gradient(ellipse at 50% 62%, var(--bg-glow) 0%, var(--bg-top) 65%);
    color: var(--paper);
    text-align: center;
  }
  .frame {
    position: absolute; left: 33px; top: 28px; right: 30px; bottom: 25px;
    border: 2px solid var(--paper);
  }
  .brand-mark {
    position: absolute; left: 50%; top: 120px;
    width: 46px; height: 46px; margin-left: -23px;
    border: 3px solid var(--paper);
  }
  .brand-name {
    position: absolute; left: 0; right: 0; top: 218px;
    font-family: "Marcellus", serif; font-size: 32px; letter-spacing: 10px;
  }
  .headline-band {
    position: absolute; left: 111px; top: 289px; width: 629px; height: 131px;
    background: var(--paper); color: var(--ink);
    font-family: "Marcellus", serif; font-size: 122px; line-height: 138px;
    letter-spacing: -1px;
  }
  .headline-sale {
    position: absolute; left: 0; right: 0; top: 420px;
    font-family: "Marcellus", serif; font-size: 248px; line-height: 250px;
    color: var(--sale-red); letter-spacing: -6px;
  }
  .hours {
    position: absolute; left: 0; right: 0;
    font-family: "Varela Round", sans-serif;
  }
  .hours-morning { top: 644px; font-size: 40px; }
  .hours-evening { top: 705px; font-size: 46px; }
  .location-box {
    position: absolute; left: 133px; top: 786px; width: 602px; height: 96px;
    border: 2px solid var(--sale-red);
  }
  .location-he {
    display: block; margin-top: 6px;
    font-family: "Varela Round", sans-serif; font-size: 34px; line-height: 42px;
  }
  .location-en {
    display: block;
    font-family: "Marcellus", serif; font-size: 29px; line-height: 38px;
  }
  .directions {
    position: absolute; left: 0; right: 0;
    font-family: "Varela Round", sans-serif; font-size: 30px;
  }
  .directions-note { top: 900px; }
  .directions-street { top: 944px; }
  .buses {
    position: absolute; left: 0; right: 0; top: 988px;
    font-family: "Marcellus", serif; font-size: 26px;
  }
  .contact-label {
    position: absolute; left: 0; right: 0; top: 1038px;
    font-family: "Varela Round", sans-serif; font-size: 22px; color: var(--sale-red);
  }
  .phone {
    position: absolute; left: 0; right: 0; top: 1068px;
    font-family: "Varela Round", sans-serif; font-size: 40px; letter-spacing: -1px;
  }
  .website {
    position: absolute; left: 0; right: 0; top: 1126px;
    font-family: "Varela Round", sans-serif; font-size: 14px; letter-spacing: 0.5px;
  }
</style>
</head>
<body>
  <main class="flyer">
    <div class="frame"></div>

    <div class="brand-mark"></div>
    <div class="brand-name">LUMELLA</div>

    <div class="headline-band">SUMMER</div>
    <div class="headline-sale">SALE</div>

    <div class="hours hours-morning">S-Th- 10:30-12:30</div>
    <div class="hours hours-evening" dir="rtl">א-ה 22:30 - 20:30</div>

    <div class="location-box">
      <span class="location-he" dir="rtl">מרכז מסחרי גבעת הדקל</span>
      <span class="location-en">HADEKEL HILL SHOPPING CENTER</span>
    </div>

    <div class="directions directions-note" dir="rtl">(מעל המאפייה)</div>
    <div class="directions directions-street" dir="rtl">ניתן להגיע גם משדרות הדקל 16</div>
    <div class="buses">Buses 21, 22, 39, 41, 45, 52, 59, 65, 68, 69, 77</div>

    <div class="contact-label">CONTACT US</div>
    <div class="phone">1.555.014.2290</div>
    <div class="website">WWW.LUMELLASTORE.COM</div>
  </main>
</body>
</html>
```